Harbor Sushi & Steak Dinner Menu

I'm looking for a MENU design with a particular feel. I want to have a base template made that I can then use for future alterations to the menu; ie I can go in and change out different entrees as the menu changes but the template will remain the same. (Ideally it would be in an Apple Pages format.). Also ideally - dinner menu will occupy 2 pages 8.5 x 11. The restaurant's name is Harbor. It is a MODERN steak house that will also feature Sushi, a Raw Bar, Exquisite Cocktails and a sophisticated nightlife crowd. I have attached our LOGO, a secondary logo that we will be featuring throughout the project including on the menu cover (the gold U). Finally - I have attached the content that we would like to see. AGAIN - I REITERATE: High end dining and lounge atmosphere. A couple of restaurants / menus that I love are Morvendel in NYC and Pellucid Steakhouse in Long Island NY. Please do not duplicate - just trying to offer some suggestions.

Requirements
Must have
• A sophisticated and elegant feel without being stuffy or old.

```html
<!DOCTYPE html>
<html lang="en">
<head>
<meta charset="utf-8">
<title>Harbor Sushi &amp; Steak — Dinner Menu</title>
<link href="https://fonts.googleapis.com/css2?family=Josefin+Sans:wght@300;400;600&family=Passion+One:wght@400&display=swap" rel="stylesheet">
<style>
  :root {
    --backdrop: #d6d2cf;
    --charcoal: #2c2c2e;
    --charcoal-deep: #1b1b1c;
    --charcoal-soft: #3a3a3c;
    --paper: #ffffff;
    --gold: #c4ad6a;
    --gold-line: #b9a46a;
    --red: #c0141c;
    --bullet: #d9532a;
    --ink: #2b2b2b;
    --ink-soft: #5b5b5b;
    --light-text: #f0ede6;
  }
  * { box-sizing: border-box; margin: 0; padding: 0; }
  html, body { width: 1200px; height: 900px; overflow: hidden; }
  body {
    background: var(--backdrop);
    font-family: "Josefin Sans", "Century Gothic", sans-serif;
    position: relative;
  }
  .page { position: absolute; top: 247px; height: 405px; overflow: hidden; }

  /* Cover spread */
  .cover-back { left: 30px; width: 277px;
    background: linear-gradient(90deg, #4a4a4c 0%, #2a2a2b 45%, var(--charcoal-deep) 100%); }
  .cover-front { left: 307px; width: 278px;
    background: linear-gradient(90deg, #232324 0%, var(--charcoal) 40%, var(--charcoal-soft) 100%);
    border-left: 1px solid #5a5a5c; }
  .cover-ribbon { position: absolute; left: 32px; top: 0; width: 61px; height: 112px; }
  .cover-name {
    position: absolute; left: 0; right: 0; top: 172px; text-align: center;
    color: var(--gold); font-weight: 300; font-size: 30px; letter-spacing: 6px;
  }

  /* Inside spread */
  .inside-left { left: 615px; width: 278px; background: var(--paper); }
  .inside-right { left: 893px; width: 277px;
    background: linear-gradient(180deg, var(--charcoal) 0%, #303032 100%); }

  .brand-name {
    position: absolute; left: 13px; top: 28px;
    color: var(--gold); font-weight: 300; font-size: 19px; letter-spacing: 3px;
  }

  .photo { position: absolute; }
  .photo-sashimi { left: 124px; top: 0; width: 154px; height: 188px;
    background: linear-gradient(160deg, #f4f4f6 0%, #e9e6e4 35%, #f08a5d 65%, #e96a3c 85%, #2e3b22 100%); }
  .photo-nigiri { left: 3px; top: 193px; width: 112px; height: 54px; border-radius: 40%;
    background: radial-gradient(ellipse at 45% 55%, #f49a6c 0%, #f3ece2 45%, #6b8a3a 70%, #ffffff 100%); }
  .photo-classic { left: 158px; top: 265px; width: 119px; height: 94px;
    background: linear-gradient(135deg, #f7f3ea 0%, #f5c84a 40%, #eaa02e 65%, #f7f1e6 100%); }
  .photo-special { left: 150px; top: 3px; width: 127px; height: 100px;
    background: linear-gradient(150deg, #3a3a3c 0%, #f2f2f2 35%, #e0b25a 60%, #1d1d1d 80%, #eeeeee 100%); }
  .photo-platter { left: 115px; top: 289px; width: 162px; height: 97px; border-radius: 50% 50% 45% 45%;
    background: radial-gradient(ellipse at 55% 50%, #e9733d 0%, #c8491f 35%, #2f3c2b 60%, #f1f1f1 80%, #303032 100%); }

  .section-title {
    position: absolute; display: flex; align-items: center; gap: 4px;
    font-family: "Passion One", "Arial Black", sans-serif;
    color: var(--red); font-size: 13px; letter-spacing: 1px; line-height: 1;
  }
  .section-title .tab { width: 16px; height: 8px; background: var(--gold); display: inline-block; }
  .section-title .rule { height: 1px; background: var(--gold-line); display: inline-block; }

  .item-list { position: absolute; list-style: none; font-size: 4.6px; line-height: 7.9px; color: var(--ink); }
  .item-list li { position: relative; padding-left: 10px; white-space: nowrap; }
  .item-list li::before {
    content: ""; position: absolute; left: 0; top: 2px; width: 2.5px; height: 3px;
    background: var(--bullet); border-radius: 1px;
  }
  .item-list li.plain::before { display: none; }
  .item-list b { font-weight: 600; }
  .item-list span { color: var(--ink-soft); }

  .inside-right .item-list { color: var(--light-text); }
  .inside-right .item-list span { color: #c9c6c0; }
  .item-list.align-right { text-align: right; }
  .item-list.align-right li { padding-left: 0; padding-right: 10px; }
  .item-list.align-right li::before { left: auto; right: 0; }

  .platter-sizes { position: absolute; right: 54px; top: 208px; text-align: right;
    font-size: 4.4px; line-height: 6px; color: var(--ink); }
  .platter-sizes b { font-weight: 600; }
  .platter-sizes p { margin-bottom: 1px; }

  .note { position: absolute; font-size: 4.2px; line-height: 8px; color: #c9c6c0; text-align: right; }
  .platter-copy { position: absolute; left: 31px; top: 292px; font-size: 5.6px; line-height: 7px; color: var(--light-text); }
</style>
</head>
<body>

<!-- Cover spread -->
<section class="page cover-back" aria-label="Back cover"></section>
<section class="page cover-front" aria-label="Front cover">
  <svg class="cover-ribbon" viewBox="0 0 61 112" aria-hidden="true">
    <defs>
      <linearGradient id="ribbonFill" x1="0" y1="0" x2="0" y2="1">
        <stop offset="0" stop-color="#b9a46a"/>
        <stop offset="1" stop-color="#8a3c22"/>
      </linearGradient>
    </defs>
    <polygon points="0,0 61,0 61,112 30.5,102 0,112" fill="url(#ribbonFill)"/>
  </svg>
  <div class="cover-name">HARBOR</div>
</section>

<!-- Inside spread: left page -->
<section class="page inside-left" aria-label="Menu page one">
  <div class="photo photo-sashimi" role="img" aria-label="Photo of sushi rolls and sashimi on a white plate with chopsticks and soy sauce"></div>
  <div class="brand-name">HARBOR</div>

  <h2 class="section-title" style="left:13px; top:82px;"><span class="tab"></span>SUSHI / SASHIMI</h2>
  <ul class="item-list" style="left:33px; top:105px;">
    <li><b>Toro:</b> <span>blue fin tuna belly (gf) Unagi;</span></li>
    <li><b>fresh water eel</b></li>
    <li><b>Ebi:</b> <span>cooked shrimp</span></li>
    <li><b>Sake:</b> <span>salmon</span></li>
    <li><b>Hamachi:</b> <span>yellowtail</span></li>
    <li><b>Madai:</b> <span>red snapper</span></li>
    <li><b>Uni:</b> <span>sea urchin</span></li>
    <li><b>Maguro:</b> <span>tuna</span></li>
    <li><b>Hirame:</b> <span>fluke</span></li>
  </ul>

  <div class="photo photo-nigiri" role="img" aria-label="Photo of assorted nigiri sushi and rolls"></div>
  <h2 class="section-title" style="left:100px; top:186px;"><span class="rule" style="width:40px;"></span>SUSHI PLATTERS<span class="tab"></span></h2>
  <div class="platter-sizes">
    <p><b>Small:</b></p>
    <p>Five Pieces assorted sushi, nine pieces sashimi, spicy tuna roll (gf)</p>
    <p style="margin-top:3px;"><b>Large:</b></p>
    <p>Eight Pieces assorted sushi, eighteen pieces of sashimi, alaskan roll, rainbow roll (gf)</p>
  </div>

  <div class="photo photo-classic" role="img" aria-label="Photo of yellow tobiko-topped classic sushi rolls"></div>
  <h2 class="section-title" style="left:13px; top:271px;"><span class="tab"></span>CLASSIC ROLLS<span class="rule" style="width:118px;"></span></h2>
  <ul class="item-list" style="left:33px; top:289px;">
    <li><b>Yellowtail:</b> <span>inside out roll with scallions (gf)</span></li>
    <li class="plain"><span>Spicy Tuna or Salmon or Yellowtail; spicy mayo</span></li>
    <li><b>California:</b> <span>crab meat, cucumber and avocado (gf)</span></li>
    <li><b>Vegetable:</b> <span>avocado, cucumber, asparagus and pickled radish (gf)</span></li>
    <li><b>Spider:</b> <span>soft shell crab and avocado with eel sauce</span></li>
    <li><b>Shrimp Tempura:</b> <span>deep fried tempura shrimp and eel sauce</span></li>
    <li class="plain"><span>Alaskan; salmon and avocado (gf)</span></li>
  </ul>
</section>

<!-- Inside spread: right page -->
<section class="page inside-right" aria-label="Menu page two">
  <div class="photo photo-special" role="img" aria-label="Photo of special sushi rolls with dipping sauce on a white dish"></div>
  <h2 class="section-title" style="left:8px; top:47px;"><span class="tab"></span>SPECIAL ROLLS<span class="rule" style="width:18px;"></span></h2>
  <ul class="item-list" style="left:22px; top:89px;">
    <li><b>The Harbor:</b> <span>tuna, salmon, yellowtail, avocado, spicy mayo, soy bean paper</span></li>
    <li><b>King Crab Rainbow:</b> <span>king crab, avocado, cucumbers, assorted fish on top</span></li>
    <li><b>Empress:</b> <span>Shrimp tempura, spicy tuna on top, eel sauce, spicy mayo</span></li>
    <li><b>Spicy Girl:</b> <span>Spicy crunchy crab meat, cucumber, shrimp on top</span></li>
    <li><b>Dragon:</b> <span>Eel, cucumber, avocado, and tobiko on top, eel sauce</span></li>
    <li><b>Yummy:</b> <span>spicy crunchy salmon, avocado, mango and salmon on top</span></li>
    <li><b>No. 9:</b> <span>Shrimp tempura, avocado, kani, spicy mayo, tobiko</span></li>
    <li><b>Sunrise Roll:</b> <span>spicy crunchy tuna and avocado, spicy crunchy salmon on top</span></li>
  </ul>

  <h2 class="section-title" style="left:31px; top:164px;"><span class="rule" style="width:88px;"></span>SEAFOOD RAW BAR<span class="tab"></span></h2>
  <ul class="item-list align-right" style="right:31px; top:185px;">
    <li><b>Lobster Cocktail</b></li>
    <li><b>Shrimp Cocktail</b></li>
    <li><b>Clams on the Half Shell</b></li>
    <li><b>Oysters on the Half Shell</b></li>
    <li><b>Colossal Crab Cocktail</b></li>
  </ul>
  <p class="note" style="right:40px; top:232px;">Raw Bar Plate for One: Two Shrimp, Half of a One Pound Lobster,<br>Two Clams, One East Coast Oyster, One West Coast Oyster</p>

  <h2 class="section-title" style="left:11px; top:272px;"><span class="tab"></span>SEAFOOD PLATTERS<span class="rule" style="width:92px;"></span></h2>
  <p class="platter-copy">Shrimp, Oysters, Clams, Lobster and Crab<br>Large or Colossal</p>
  <div class="photo photo-platter" role="img" aria-label="Photo of a seafood platter with crab, mussels, shrimp and lemon"></div>
</section>

</body>
</html>
```